Custom open/closed sign for our young jewellery and silk shop

We are a new jewellery and silk store in Wellington, New Zealand specialising in products sourced from Suzhou, China.

We're after a design for an open/closed sign for our door. I know it sounds odd, but we want to put a bit of effort into making it special.

We've been thinking about designs relating to round Chinese garden moon gates with doors, to match with our round logo in some way, but are open to other ideas.

Our font is Avenir, so try to work with that if you can.

Have attached our logos on black/white for reference.

Target Market(s)

People gazing at our door - people in a hurry, people who don't know who we are, etc

Industry/Entity Type

Jewelry Store

Font styles to use
Other font styles liked:
• Avenir Pro

Colors
fece3e
ffffff
000000

Requirements
Must have
• The words "open" and "closed" on each side, possibly with "We are" or "Sorry we're" or something similar.
• Needs to fit within a 300mm square area, but if it's rectangular, aim for a 300x130mm kind of size.
• Writing should be in Avenir and letter spaced similarly to our logo.
Nice to have
• We like the idea of Chinese moon gate (https://en.brollapedia.net/wiki/Ring_door) to fit with our overall Chinese/oriental theme.
• On a black background is probably preferred, but not essential.
Should not have
• Colours that vastly don't match our black/white/yellow theme.

```html
<!DOCTYPE html>
<html lang="en">
<head>
<meta charset="utf-8">
<title>Jade Lane – Open / Closed Door Sign</title>
<link rel="stylesheet" href="https://fonts.googleapis.com/css2?family=Figtree:wght@400;500;800&display=swap">
<style>
  :root {
    --brand-yellow: #fece3e;
    --brand-black: #000000;
    --brand-white: #ffffff;
    --backdrop: #dcdcd8;
    --shadow: rgba(0, 0, 0, 0.28);
  }
  * { margin: 0; padding: 0; box-sizing: border-box; }
  html, body {
    width: 1200px; height: 1200px; overflow: hidden;
    background: var(--backdrop);
    font-family: "Figtree", "Avenir Next", sans-serif;
  }
  .canvas { position: relative; width: 1200px; height: 1200px; }

  .sign {
    position: absolute; left: 212px; width: 828px; height: 366px;
    overflow: hidden;
    box-shadow: 10px 12px 18px var(--shadow);
  }
  .sign--open { top: 144px; background: var(--brand-white); }
  .sign--closed { top: 748px; background: var(--brand-black); }

  .sign__band {
    position: absolute; left: 0; right: 0; bottom: 0; height: 79px;
    display: flex; align-items: center; justify-content: flex-end;
    padding-right: 64px; gap: 12px;
  }
  .sign--open .sign__band { background: var(--brand-black); }
  .sign--closed .sign__band { background: var(--brand-white); }

  .moon-gate {
    position: absolute; left: 47px; top: 43px; width: 292px; height: 292px;
    border-radius: 50%;
    display: flex; flex-direction: column; align-items: center; justify-content: center;
    font-weight: 500; font-size: 46px; line-height: 1.15; letter-spacing: 0.14em;
    text-indent: 0.14em;
  }
  .sign--open .moon-gate { background: var(--brand-black); color: var(--brand-white); }
  .sign--closed .moon-gate { background: var(--brand-white); color: var(--brand-black); }

  .message {
    position: absolute; left: 366px;
    font-weight: 800; line-height: 1; white-space: nowrap;
  }
  .message__lead, .message__state { display: block; letter-spacing: 0.01em; }
  .message__state { color: var(--brand-yellow); }

  .sign--open .message { top: 58px; }
  .sign--open .message__lead { font-size: 52px; color: var(--brand-black); }
  .sign--open .message__state { font-size: 138px; margin-top: 0; margin-left: -4px; }

  .sign--closed .message { top: 64px; }
  .sign--closed .message__lead { font-size: 62px; color: var(--brand-white); }
  .sign--closed .message__state { font-size: 104px; margin-top: 2px; margin-left: -3px; }

  .wordmark__dot {
    width: 26px; height: 26px; border-radius: 50%;
    border: 2px solid var(--brand-yellow);
  }
  .wordmark__name {
    font-weight: 500; font-size: 15px; letter-spacing: 0.42em;
  }
  .sign--open .wordmark__name { color: var(--brand-white); }
  .sign--closed .wordmark__name { color: var(--brand-black); }
</style>
</head>
<body>
<main class="canvas">

  <section class="sign sign--open" aria-label="Open side">
    <div class="sign__band">
      <span class="wordmark__dot"></span>
      <span class="wordmark__name">JADE LANE</span>
    </div>
    <div class="moon-gate"><span>JADE</span><span>LANE</span></div>
    <p class="message">
      <span class="message__lead">COME IN WE'RE</span>
      <span class="message__state">OPEN</span>
    </p>
  </section>

  <section class="sign sign--closed" aria-label="Closed side">
    <div class="sign__band">
      <span class="wordmark__dot"></span>
      <span class="wordmark__name">JADE LANE</span>
    </div>
    <div class="moon-gate"><span>JADE</span><span>LANE</span></div>
    <p class="message">
      <span class="message__lead">SORRY WE'RE</span>
      <span class="message__state">CLOSED</span>
    </p>
  </section>

</main>
</body>
</html>
```